Reed & Vale NC grand opening (for BILLBOARD)

Advertising the grand opening of our cannabis/hemp shop in NC. We will sell all things hemp (flower, cartridges, disposables, edibles, creams, lotions, pet products etc...)

Requirements
Must have
• include, open starting Aug 1, but grand opening Aug 15th.
Nice to have
• Difference slogan ideas "Save some cash, buy our grass" "Find your perfect high at Reed & Vale cannabis store" "Experience Nature's Gift: Reed & Vale Cannabis Store"

```html
<!DOCTYPE html>
<html lang="en">
<head>
<meta charset="utf-8">
<title>Reed &amp; Vale Billboard</title>
<link rel="stylesheet" href="https://fonts.googleapis.com/css2?family=Montserrat:wght@600;700&display=swap">
<style>
  :root {
    --backdrop: #b4b3b3;
    --board-white: #ffffff;
    --navy: #12113a;
    --leaf-green: #6cc04a;
    --text-white: #ffffff;
  }
  * { margin: 0; padding: 0; box-sizing: border-box; }
  html, body {
    width: 1200px;
    height: 1200px;
    overflow: hidden;
    background: var(--backdrop);
    font-family: "Montserrat", Arial, sans-serif;
  }
  .canvas {
    position: relative;
    width: 1200px;
    height: 1200px;
    display: flex;
    align-items: center;
    justify-content: center;
  }
  .billboard {
    position: relative;
    width: 1100px;
    height: 324px;
    background: var(--board-white);
    box-shadow: 0 2px 4px rgba(0,0,0,0.25);
    overflow: hidden;
  }
  .billboard-swoosh {
    position: absolute;
    inset: 0;
    width: 100%;
    height: 100%;
  }
  .swoosh-navy { fill: var(--navy); }
  .swoosh-green { fill: var(--leaf-green); }
  .brand {
    position: absolute;
    top: 40px;
    left: 0;
    right: 0;
    display: flex;
    align-items: center;
    justify-content: center;
    gap: 16px;
  }
  .brand-dot {
    width: 24px;
    height: 24px;
    border-radius: 50%;
    background: var(--leaf-green);
  }
  .brand-name {
    font-weight: 600;
    font-size: 72px;
    line-height: 1;
    color: var(--navy);
    letter-spacing: -1px;
  }
  .dates {
    position: absolute;
    top: 126px;
    left: 0;
    right: 0;
    text-align: center;
    font-weight: 700;
    font-size: 20px;
    line-height: 1;
    letter-spacing: 1px;
    color: var(--navy);
  }
  .dates-accent { color: var(--leaf-green); }
  .location {
    position: absolute;
    top: 206px;
    left: 0;
    right: 0;
    text-align: center;
    font-weight: 700;
    font-size: 31px;
    line-height: 1.2;
    letter-spacing: 0.5px;
    color: var(--text-white);
  }
  .slogan {
    position: absolute;
    top: 250px;
    left: 0;
    right: 0;
    text-align: center;
    font-weight: 700;
    font-size: 52px;
    line-height: 1;
    letter-spacing: 1px;
    color: var(--text-white);
  }
  .slogan-accent { color: var(--leaf-green); }
</style>
</head>
<body>
  <main class="canvas">
    <section class="billboard" aria-label="Reed &amp; Vale billboard">
      <svg class="billboard-swoosh" viewBox="0 0 1100 324" preserveAspectRatio="none" aria-hidden="true">
        <path class="swoosh-green" d="M260,168 Q700,150 1100,196 L1100,212 Q700,168 260,168 Z"/>
        <path class="swoosh-navy" d="M0,200 Q450,162 860,176 Q450,174 0,214 Z"/>
        <path class="swoosh-navy" d="M0,228 Q520,178 1100,214 L1100,324 L0,324 Z"/>
      </svg>

      <div class="brand">
        <span class="brand-dot" aria-hidden="true"></span>
        <span class="brand-name">Reed &amp; Vale</span>
      </div>

      <p class="dates">OPEN AUG 1 &middot; <span class="dates-accent">GRAND OPENING AUG 15</span></p>

      <p class="location">OFF EXIT 6A BIRCHWOOD RD</p>
      <p class="slogan"><span class="slogan-accent">SAVE SOME CASH</span> BUY OUR GRASS</p>
    </section>
  </main>
</body>
</html>
```